IT Services Company Needs Corporate PPT Template

This is urgent (need a fast turn around). We need a corporate PPT template deck (NOTE: Deck should be in 4:3 ratio) for our IT Services firm that is clean but slick and modern. We tend to lean more towards the flat design look. I'm attaching a zip file which includes our Corporate Branding Guide (which is in progress), color scheme, A PPT deck as inspiration (our logo is on the last slide), our font (LATO). Our newly launched website is located at: http://www.veltrani.com.

As an example of a deck we like see: http://stockpanel.net/item/clean-multipurpose-business-presentation-template/5218830?WT.ac=category_thumb&WT.seg_1=category_thumb&WT.z_author=BrimLayouts
Although we don't want "this" deck - it gives an idea of style.

I'm also attaching a copy of our corporate deck as it is now to give you an idea of the type of content that would appear on various slides. We definitely want the following slides (at least) within the template:

Title Slide
Blank Slide
2 Column - with bullets
2 Column - no bullets
Single Column - no bullets
Single Column - with bullets
Various Charts and Tables (see example deck)
Meet the Team
Offering Slide
Customer Showcase
Timeline
Case Study
Contact US

Note: Being awarded this job will lead to a second job of creating our corporate deck.

CIO, CEO, Technology Officers, Sales People, Marketing, IT heads and staff, Customers, Prospective customers

Business

• See description and attached files

```html
<!DOCTYPE html>
<html lang="en">
<head>
<meta charset="utf-8">
<title>Veltrani – Single Column with Bullets</title>
<link href="https://fonts.googleapis.com/css2?family=Lato:wght@400;700;900&display=swap" rel="stylesheet">
<style>
  :root {
    --band-dark: #00507a;
    --band-mid: #0b6390;
    --band-light: #1a76a3;
    --title-tint: #a8d3ea;
    --subtitle-blue: #3a8fc0;
    --bullet-navy: #123f66;
    --body-grey: #666a6e;
    --page-white: #ffffff;
    --page-mist: #ededed;
    --footer-white: #ffffff;
  }
  * { box-sizing: border-box; margin: 0; padding: 0; }
  html, body { width: 1200px; height: 900px; overflow: hidden; }
  body {
    font-family: "Lato", sans-serif;
    background: var(--page-white);
  }
  .slide {
    position: relative;
    width: 1200px;
    height: 900px;
    background: linear-gradient(to bottom, var(--page-mist) 87px, var(--page-white) 150px, var(--page-white) 740px, var(--page-mist) 840px);
  }
  .header-band {
    position: absolute; left: 0; top: 0;
    width: 1200px; height: 87px;
    background: linear-gradient(to right, var(--band-mid), var(--band-dark) 60%, var(--band-mid));
  }
  .header-notch {
    position: absolute; left: 54px; top: 86px;
    width: 44px; height: 22px;
  }
  .slide-title {
    position: absolute; left: 27px; top: 19px;
    font-size: 39px; font-weight: 700;
    color: var(--title-tint);
    letter-spacing: -0.3px;
  }
  .subtitle {
    position: absolute; left: 63px; top: 156px;
    font-size: 31px; font-weight: 700;
    color: var(--subtitle-blue);
  }
  .bullet-list {
    position: absolute; left: 62px; top: 230px;
    list-style: none;
  }
  .bullet-list li {
    display: flex; align-items: center;
    height: 40px; margin-bottom: 38.5px;
    font-size: 24px; font-weight: 700;
    color: var(--body-grey);
  }
  .bullet-mark {
    width: 33px; height: 30px; margin-right: 16px;
    flex: none;
  }
  .footer-band {
    position: absolute; left: 0; top: 840px;
    width: 1200px; height: 60px;
    background: linear-gradient(to right, var(--band-light), var(--band-mid) 50%, var(--band-light));
    border-top: 2px solid var(--band-dark);
  }
  .brand-name {
    position: absolute; left: 21px; top: 852px;
    font-size: 32px; font-weight: 900;
    color: var(--footer-white);
    letter-spacing: 0.5px;
  }
  .connect-label {
    position: absolute; left: 819px; top: 864px;
    font-size: 15px; font-weight: 700;
    color: var(--footer-white);
  }
  .social-links {
    position: absolute; left: 982px; top: 856px;
    display: flex; align-items: center;
  }
  .social-slot {
    width: 20px; height: 20px;
    background: var(--footer-white);
    border-radius: 3px;
    margin: 0 8px;
  }
  .social-divider {
    width: 2px; height: 30px;
    background: var(--footer-white);
  }
</style>
</head>
<body>
  <main class="slide">
    <div class="header-band" role="img" aria-label="Deep blue title band with a faint hexagon texture"></div>
    <svg class="header-notch" viewBox="0 0 44 22" aria-hidden="true">
      <polygon points="0,0 44,0 22,22" fill="var(--band-dark)"/>
    </svg>
    <h1 class="slide-title">Project Title Here</h1>

    <h2 class="subtitle">Subtitle text here</h2>

    <ul class="bullet-list">
      <li><svg class="bullet-mark" viewBox="0 0 33 30" aria-hidden="true"><rect width="33" height="30" fill="var(--bullet-navy)"/><polyline points="13,8 20,15 13,22" fill="none" stroke="#fff" stroke-width="3.5"/></svg>Lorem ipsum dolor sit ipsum Lorem ipsuma dolor sit ipsum</li>
      <li><svg class="bullet-mark" viewBox="0 0 33 30" aria-hidden="true"><rect width="33" height="30" fill="var(--bullet-navy)"/><polyline points="13,8 20,15 13,22" fill="none" stroke="#fff" stroke-width="3.5"/></svg>Lorem ipsum dolor sit ipsum Lorem ipsuma dolor sit ipsum</li>
      <li><svg class="bullet-mark" viewBox="0 0 33 30" aria-hidden="true"><rect width="33" height="30" fill="var(--bullet-navy)"/><polyline points="13,8 20,15 13,22" fill="none" stroke="#fff" stroke-width="3.5"/></svg>Lorem ipsum dolor sit ipsum Lorem ipsuma dolor sit ipsum</li>
      <li><svg class="bullet-mark" viewBox="0 0 33 30" aria-hidden="true"><rect width="33" height="30" fill="var(--bullet-navy)"/><polyline points="13,8 20,15 13,22" fill="none" stroke="#fff" stroke-width="3.5"/></svg>Lorem ipsum dolor sit ipsum Lorem ipsuma dolor sit ipsum</li>
      <li><svg class="bullet-mark" viewBox="0 0 33 30" aria-hidden="true"><rect width="33" height="30" fill="var(--bullet-navy)"/><polyline points="13,8 20,15 13,22" fill="none" stroke="#fff" stroke-width="3.5"/></svg>Lorem ipsum dolor sit ipsum Lorem ipsuma dolor sit ipsum</li>
      <li><svg class="bullet-mark" viewBox="0 0 33 30" aria-hidden="true"><rect width="33" height="30" fill="var(--bullet-navy)"/><polyline points="13,8 20,15 13,22" fill="none" stroke="#fff" stroke-width="3.5"/></svg>Lorem ipsum dolor sit ipsum Lorem ipsuma dolor sit ipsum</li>
      <li><svg class="bullet-mark" viewBox="0 0 33 30" aria-hidden="true"><rect width="33" height="30" fill="var(--bullet-navy)"/><polyline points="13,8 20,15 13,22" fill="none" stroke="#fff" stroke-width="3.5"/></svg>Lorem ipsum dolor sit ipsum Lorem ipsuma dolor sit ipsum</li>
    </ul>

    <footer>
      <div class="footer-band" role="img" aria-label="Blue footer band with a faint hexagon texture"></div>
      <div class="brand-name">Veltrani</div>
      <div class="connect-label">CONNECT WITH US:</div>
      <nav class="social-links" aria-label="Social channels">
        <span class="social-slot"></span>
        <span class="social-divider"></span>
        <span class="social-slot"></span>
        <span class="social-divider"></span>
        <span class="social-slot"></span>
        <span class="social-divider"></span>
        <span class="social-slot"></span>
        <span class="social-divider"></span>
        <span class="social-slot"></span>
      </nav>
    </footer>
  </main>
</body>
</html>
```